Iron Pivot Hoops Academy- Small Group and Private Lessons

I would like to advertise and drive my small group basketball lessons (offered on Fridays during the summer in Prosper, Texas with the following four groups- 1. Middle School Girls Small Group, 2. Middle School Boys Small Group, 3. High School Girls Small Group, 4. High School Boys Small Group).
Tag Line- "Do you want to become a complete player?"
We work to make each player as well rounded as possible by focusing on: balanced footwork, ballhandling, dribbling, finishing, passing, shooting, moving without the ball, basketball IQ
Website- www.ironpivothoopsacademy.com

```html
<!DOCTYPE html>
<html lang="en">
<head>
<meta charset="utf-8">
<title>Iron Pivot Hoops Academy – Small Group Lessons</title>
<link rel="stylesheet" href="https://fonts.googleapis.com/css2?family=Anton&family=Open+Sans:wght@400;700&family=Roboto:ital,wght@0,400;0,500;1,700;1,900&family=Roboto+Condensed:wght@400;500&display=swap">
<style>
  :root {
    --page-bg: #e4e4e4;
    --flyer-black: #000000;
    --headline-top: #f7a61c;
    --headline-bottom: #f0661e;
    --accent-orange: #f36f21;
    --soft-gray: #c9c9c9;
    --list-gray: #b5b5b5;
    --band-top: #f6a21f;
    --band-bottom: #f0721f;
    --footer-red: #e5452a;
    --ink-dark: #2a1206;
    --white: #ffffff;
    --badge-red: #c7321c;
  }
  * { margin: 0; padding: 0; box-sizing: border-box; }
  html, body {
    width: 1200px; height: 1200px; overflow: hidden;
    background: var(--page-bg);
  }
  .flyer {
    position: absolute; left: 175px; top: 51px;
    width: 850px; height: 1098px;
    background: var(--flyer-black);
    overflow: hidden;
    box-shadow: 0 6px 18px rgba(0,0,0,0.25);
  }
  .headline {
    position: absolute; left: 0; top: 36px; width: 100%;
    text-align: center;
    font-family: "Anton", sans-serif;
    font-size: 72px; line-height: 80px; letter-spacing: 1px;
    background: linear-gradient(180deg, var(--headline-top), var(--headline-bottom));
    -webkit-background-clip: text; background-clip: text; color: transparent;
  }
  .brand-stack {
    position: absolute; left: 38px; top: 250px;
    font-family: "Open Sans", sans-serif; color: var(--white);
  }
  .brand-stack .brand-lead { font-weight: 700; font-size: 62px; line-height: 74px; }
  .brand-stack .brand-line { font-weight: 400; font-size: 52px; line-height: 60px; }
  .hoop-art {
    position: absolute; left: 459px; top: 236px; width: 391px; height: 446px;
    background: radial-gradient(circle at 55% 70%, #b5501f 0%, #7a2f12 35%, #2a0f05 65%, var(--flyer-black) 85%);
  }
  .lessons {
    position: absolute; left: 32px; top: 530px;
    display: flex; align-items: center; gap: 16px;
  }
  .ball-icon {
    width: 70px; height: 70px; border-radius: 50%;
    background: radial-gradient(circle at 40% 40%, #e9792c, #a8401a);
    border: 4px solid var(--white);
  }
  .lessons-title {
    font-family: "Roboto", sans-serif; font-weight: 500;
    color: var(--accent-orange); font-size: 34px; line-height: 43px;
  }
  .offer-line {
    position: absolute; left: 34px; top: 625px;
    font-family: "Roboto Condensed", sans-serif; font-size: 24px;
    color: var(--soft-gray);
  }
  .offer-emph {
    position: absolute; left: 34px; top: 665px;
    font-family: "Roboto Condensed", sans-serif; font-weight: 500; font-size: 34px;
    color: var(--accent-orange);
  }
  .groups {
    position: absolute; top: 724px; list-style: none;
    font-family: "Roboto Condensed", sans-serif; font-size: 23px; line-height: 35px;
    color: var(--list-gray);
  }
  .groups.left { left: 40px; }
  .groups.right { left: 455px; top: 726px; }
  .focus-band {
    position: absolute; left: 0; top: 803px; width: 100%; height: 242px;
    background: linear-gradient(180deg, var(--band-top), var(--band-bottom));
  }
  .focus-title {
    position: absolute; left: 36px; top: 18px;
    font-family: "Roboto", sans-serif; font-style: italic; font-weight: 900;
    font-size: 26px; line-height: 36px; color: var(--ink-dark);
  }
  .skills {
    position: absolute; top: 96px; list-style: none;
    font-family: "Roboto", sans-serif; font-size: 23px; line-height: 31px;
    color: var(--ink-dark);
  }
  .skills.col-a { left: 36px; }
  .skills.col-b { left: 272px; top: 100px; }
  .skills li { display: flex; align-items: center; gap: 6px; }
  .tick { width: 14px; height: 14px; flex: none; }
  .academy-mark {
    position: absolute; left: 590px; top: 18px; width: 220px;
    display: flex; flex-direction: column; align-items: center; gap: 10px;
  }
  .academy-mark .mark-circle {
    width: 120px; height: 120px; border-radius: 50%; background: var(--badge-red);
  }
  .academy-mark .mark-name {
    font-family: "Roboto", sans-serif; font-weight: 500; font-size: 22px; line-height: 26px;
    color: var(--ink-dark); text-align: center;
  }
  .footer-bar {
    position: absolute; left: 0; top: 1045px; width: 100%; height: 53px;
    background: var(--footer-red);
    display: flex; align-items: center; justify-content: center;
    font-family: "Roboto", sans-serif; font-style: italic; font-weight: 700;
    font-size: 20px; color: var(--white);
  }
</style>
</head>
<body>
<main class="flyer">
  <h1 class="headline">DO YOU WANT TO BECOME<br>A COMPLETE PLAYER?</h1>

  <div class="brand-stack">
    <div class="brand-lead">IRON PIVOT</div>
    <div class="brand-line">HOOPS</div>
    <div class="brand-line">ACADEMY</div>
  </div>

  <div class="hoop-art" role="img" aria-label="Basketball dropping through an orange hoop and white net"></div>

  <div class="lessons">
    <div class="ball-icon"></div>
    <div class="lessons-title">SMALL GROUP<br>BASKETBALL LESSONS</div>
  </div>

  <p class="offer-line">Offered on Fridays during the summer in Prosper,</p>
  <p class="offer-emph">Texas with the following four groups-</p>

  <ol class="groups left">
    <li>1. Middle School Girls Small Group</li>
    <li>2. Middle School Boys Small Group</li>
  </ol>
  <ol class="groups right">
    <li>3. High School Girls Small Group</li>
    <li>4. High School Boys Small Group</li>
  </ol>

  <section class="focus-band">
    <h2 class="focus-title">WE WORK TO MAKE EACH PLAYER AS WELL<br>ROUNDED AS POSSIBLE BY FOCUSING ON</h2>
    <ul class="skills col-a">
      <li><svg class="tick" viewBox="0 0 14 14"><path d="M2 7.5 L5.5 11 L12 2.5" fill="none" stroke="#fff" stroke-width="2.4" stroke-linecap="round" stroke-linejoin="round"/></svg>Balanced footwork</li>
      <li><svg class="tick" viewBox="0 0 14 14"><path d="M2 7.5 L5.5 11 L12 2.5" fill="none" stroke="#fff" stroke-width="2.4" stroke-linecap="round" stroke-linejoin="round"/></svg>Ballhandling</li>
      <li><svg class="tick" viewBox="0 0 14 14"><path d="M2 7.5 L5.5 11 L12 2.5" fill="none" stroke="#fff" stroke-width="2.4" stroke-linecap="round" stroke-linejoin="round"/></svg>Dribbling</li>
      <li><svg class="tick" viewBox="0 0 14 14"><path d="M2 7.5 L5.5 11 L12 2.5" fill="none" stroke="#fff" stroke-width="2.4" stroke-linecap="round" stroke-linejoin="round"/></svg>Finishing</li>
    </ul>
    <ul class="skills col-b">
      <li><svg class="tick" viewBox="0 0 14 14"><path d="M2 7.5 L5.5 11 L12 2.5" fill="none" stroke="#fff" stroke-width="2.4" stroke-linecap="round" stroke-linejoin="round"/></svg>Passing</li>
      <li><svg class="tick" viewBox="0 0 14 14"><path d="M2 7.5 L5.5 11 L12 2.5" fill="none" stroke="#fff" stroke-width="2.4" stroke-linecap="round" stroke-linejoin="round"/></svg>Shooting</li>
      <li><svg class="tick" viewBox="0 0 14 14"><path d="M2 7.5 L5.5 11 L12 2.5" fill="none" stroke="#fff" stroke-width="2.4" stroke-linecap="round" stroke-linejoin="round"/></svg>Moving without the ball</li>
      <li><svg class="tick" viewBox="0 0 14 14"><path d="M2 7.5 L5.5 11 L12 2.5" fill="none" stroke="#fff" stroke-width="2.4" stroke-linecap="round" stroke-linejoin="round"/></svg>Basketball IQ</li>
    </ul>
    <div class="academy-mark">
      <div class="mark-circle"></div>
      <div class="mark-name">IRON PIVOT<br>HOOPS ACADEMY</div>
    </div>
  </section>

  <footer class="footer-bar">www.ironpivothoopsacademy.com</footer>
</main>
</body>
</html>
```